Jewelry Wholesale Business Card Design

Company name: VORELIA
Business Background: Wholesale jewelry store located in downtown Los Angeles. We specialize in 18k gold-filled, stainless steel, 14kt gold, and natural stone jewelry.
website: www.vorelia-sample.com
Instagram: vorelia_
Email: sales@vorelia-sample.com
Address: 318 W. MAPLE ST #27, #109
LOS ANGELES, CA 90014
(213)555-0172

We would like to create a simple, yet elegant business card for my store
-Includes company logo
-Black background preferred
-Gold metallic color letters
- Lists the type of products we sell
-Small icons for instagram handle, phone, email, and website

Target Market(s)

Hispanic community, age 12-40

Industry/Entity Type

Jewelry Wholesale

Contact Information for Business Card

logo, business location, website, phone number, email, instagram, lists type of products, Derek Malo(my name)

Font styles to use
Serif
Sans Serif

Colors
FFF300
FFF600
FEFA6F
FFFEC7
FFFEE8

Requirements
Must have
• logo, business location, website, phone number, email, instagram, lists type of products, Derek Malo(my name)

```html
<!DOCTYPE html>
<html lang="en">
<head>
<meta charset="utf-8">
<title>VORELIA Business Card</title>
<link rel="stylesheet" href="https://fonts.googleapis.com/css2?family=Cinzel:wght@400&family=Roboto:wght@400;500&display=swap">
<style>
  :root {
    --page-bg: #2a2a2b;
    --card-bg: #141414;
    --card-edge: #0a0a0a;
    --pattern-tone: #1d1c1b;
    --gold: #d68f2c;
    --gold-light: #e8b04f;
    --gold-pale: #f0c878;
    --icon-ink: #141414;
  }
  * { box-sizing: border-box; margin: 0; padding: 0; }
  html, body {
    width: 1200px;
    height: 960px;
    overflow: hidden;
    background: var(--page-bg);
  }
  .canvas {
    position: relative;
    width: 1200px;
    height: 960px;
  }
  .card {
    position: absolute;
    left: 250px;
    width: 700px;
    height: 400px;
    background: var(--card-bg);
    border: 1px solid var(--card-edge);
    box-shadow: 0 18px 40px rgba(0,0,0,0.45);
    overflow: hidden;
  }
  .card--front { top: 50px; }
  .card--back { top: 510px; }

  .card__pattern {
    position: absolute;
    inset: 0;
    background: radial-gradient(ellipse at 70% 60%, var(--pattern-tone) 0%, var(--card-bg) 75%);
  }

  .brand {
    position: absolute;
    display: flex;
    align-items: center;
    gap: 22px;
  }
  .card--front .brand { left: 70px; top: 40px; }
  .brand__mark {
    width: 62px;
    height: 62px;
    border-radius: 50%;
    background: var(--gold);
  }
  .brand__name {
    font-family: "Cinzel", serif;
    font-weight: 400;
    font-size: 40px;
    letter-spacing: 3px;
    color: var(--gold-light);
  }

  .owner {
    position: absolute;
    left: 154px;
    top: 110px;
    font-family: "Cinzel", serif;
    font-size: 18px;
    letter-spacing: 2px;
    color: var(--gold-pale);
  }

  .back-lockup {
    position: absolute;
    inset: 0;
    display: flex;
    flex-direction: column;
    align-items: center;
    justify-content: center;
    gap: 30px;
  }
  .card--back .brand { position: static; }
  .card--back .brand__name { font-size: 46px; }
  .products {
    font-family: "Roboto", sans-serif;
    font-weight: 400;
    font-size: 14px;
    letter-spacing: 1.5px;
    color: var(--gold-pale);
    text-transform: uppercase;
  }

  .contact {
    position: absolute;
    list-style: none;
    font-family: "Roboto", sans-serif;
    font-size: 18px;
    color: var(--gold-pale);
  }
  .contact--social { left: 56px; top: 176px; }
  .contact--location { left: 360px; top: 262px; }
  .contact__row {
    display: flex;
    align-items: flex-start;
    gap: 14px;
    margin-bottom: 12px;
  }
  .contact__icon {
    flex: none;
    width: 30px;
    height: 30px;
    border-radius: 50%;
    background: var(--gold);
    display: flex;
    align-items: center;
    justify-content: center;
  }
  .contact__text { line-height: 30px; }
  .contact__text--stack { line-height: 24px; padding-top: 3px; }
</style>
</head>
<body>
<main class="canvas">

  <section class="card card--front" aria-label="Card front">
    <div class="card__pattern" role="img" aria-label="Faint repeating diamond outline pattern"></div>

    <div class="brand">
      <span class="brand__mark"></span>
      <span class="brand__name">VORELIA</span>
    </div>
    <p class="owner">Derek Malo</p>

    <ul class="contact contact--social">
      <li class="contact__row">
        <span class="contact__icon"></span>
        <span class="contact__text">vorelia_</span>
      </li>
      <li class="contact__row">
        <span class="contact__icon">
          <svg width="16" height="12" viewBox="0 0 16 12" aria-hidden="true">
            <rect x="0.5" y="0.5" width="15" height="11" fill="#141414" stroke="#141414"/>
            <polyline points="0.5,0.5 8,7 15.5,0.5" fill="none" stroke="#d68f2c" stroke-width="1.4"/>
          </svg>
        </span>
        <span class="contact__text">sales@vorelia-sample.com</span>
      </li>
    </ul>

    <ul class="contact contact--location">
      <li class="contact__row">
        <span class="contact__icon">
          <svg width="18" height="18" viewBox="0 0 18 18" aria-hidden="true" fill="none" stroke="#141414" stroke-width="1.5">
            <circle cx="9" cy="9" r="7.5"/>
            <ellipse cx="9" cy="9" rx="3.2" ry="7.5"/>
            <line x1="1.5" y1="9" x2="16.5" y2="9"/>
            <line x1="3" y1="5" x2="15" y2="5"/>
            <line x1="3" y1="13" x2="15" y2="13"/>
          </svg>
        </span>
        <span class="contact__text">www.vorelia-sample.com</span>
      </li>
      <li class="contact__row">
        <span class="contact__icon">
          <svg width="14" height="18" viewBox="0 0 14 18" aria-hidden="true">
            <path d="M7 1 C3.5 1 1 3.6 1 6.8 C1 11 7 17 7 17 C7 17 13 11 13 6.8 C13 3.6 10.5 1 7 1 Z" fill="#141414"/>
            <circle cx="7" cy="6.8" r="2.3" fill="#d68f2c"/>
          </svg>
        </span>
        <span class="contact__text contact__text--stack">
          318 W. MAPLE ST #27, #109<br>
          LOS ANGELES, CA 90014<br>
          (213)555-0172
        </span>
      </li>
    </ul>
  </section>

  <section class="card card--back" aria-label="Card back">
    <div class="card__pattern" role="img" aria-label="Faint repeating diamond outline pattern"></div>
    <div class="back-lockup">
      <div class="brand">
        <span class="brand__mark"></span>
        <span class="brand__name">VORELIA</span>
      </div>
      <p class="products">18K Gold-Filled · Stainless Steel · 14KT Gold · Natural Stone</p>
    </div>
  </section>

</main>
</body>
</html>
```